Business Card Design

We need a business card design for a Dry cleaners in Brisbane, Australia. We are trying to promote a fresh/clean image consistent with our website. www.quillpresswash.com.au

Looking for a professional neat card that's easy to read.

Target Market(s)

Customers looking for a professional, fresh and clean drycleaners.

Industry/Entity Type

Business

Contact Information for Business Card

See our existing business card. The Fax number (07) 3468 5203 to be removed.

Requirements
Must have
• All the details on current business card less the fax number.
Nice to have
• I like white text on coloured background. Blue works well as we are located near the water...

```html
<!DOCTYPE html>
<html lang="en">
<head>
<meta charset="utf-8">
<title>Quill Press Wash – Business Card</title>
<link rel="stylesheet" href="https://fonts.googleapis.com/css2?family=Exo+2:wght@400;500;700;800&display=swap">
<style>
  :root {
    --bg: #e4e5e7;
    --card: #ffffff;
    --navy: #323f91;
    --red: #e8343c;
    --name-red: #a8332f;
    --ink: #2b2b2b;
    --white: #ffffff;
  }
  * { margin: 0; padding: 0; box-sizing: border-box; }
  html, body { width: 1200px; height: 894px; overflow: hidden; }
  body {
    background: var(--bg);
    font-family: "Exo 2", sans-serif;
    display: flex;
    align-items: center;
    justify-content: center;
    gap: 60px;
  }
  .card {
    position: relative;
    width: 540px;
    height: 310px;
    background: var(--card);
    box-shadow: 0 4px 14px rgba(0,0,0,.12);
    overflow: hidden;
  }
  .accent-band {
    position: absolute;
    right: 0;
    background: var(--red);
  }
  /* Contact side */
  .card--contact .accent-band { top: 36px; width: 100px; height: 26px; }
  .identity {
    position: absolute;
    left: 170px;
    top: 52px;
    width: 260px;
  }
  .identity__name {
    font-size: 30px;
    font-weight: 500;
    letter-spacing: 1px;
    color: var(--ink);
    line-height: 1;
    white-space: nowrap;
  }
  .identity__name .first { color: var(--name-red); }
  .identity__title {
    margin-top: 8px;
    font-size: 19px;
    font-weight: 500;
    letter-spacing: 1px;
    color: var(--ink);
    white-space: nowrap;
  }
  .contact-panel {
    position: absolute;
    left: 16px;
    right: 16px;
    top: 130px;
    bottom: 16px;
    background: var(--navy);
    border-radius: 14px;
    display: grid;
    grid-template-columns: 1fr 1.35fr 1fr;
    color: var(--white);
  }
  .contact-panel__cell {
    display: flex;
    flex-direction: column;
    align-items: center;
    justify-content: center;
    gap: 12px;
    padding: 0 8px;
    text-align: center;
    font-size: 13px;
    line-height: 1.45;
    letter-spacing: .5px;
    white-space: nowrap;
  }
  .contact-panel__cell + .contact-panel__cell { border-left: 1.5px solid var(--white); }
  .contact-panel__icon { width: 30px; height: 30px; }
  /* Brand side */
  .card--brand .accent-band { top: 34px; width: 130px; height: 26px; }
  .brand {
    position: absolute;
    inset: 0;
    display: flex;
    align-items: center;
    justify-content: center;
    gap: 14px;
  }
  .brand__dot {
    width: 22px;
    height: 22px;
    border-radius: 50%;
    background: var(--navy);
  }
  .brand__name {
    font-size: 40px;
    font-weight: 800;
    color: var(--navy);
    letter-spacing: .5px;
  }
</style>
</head>
<body>
  <section class="card card--contact">
    <div class="accent-band"></div>
    <div class="identity">
      <p class="identity__name"><span class="first">DANIEL</span> HARTLEY</p>
      <p class="identity__title">CREATIVE DIRECTOR</p>
    </div>
    <div class="contact-panel">
      <div class="contact-panel__cell contact-panel__cell--phone">
        <svg class="contact-panel__icon" viewBox="0 0 32 32" fill="none" stroke="#fff" stroke-width="2.2" stroke-linejoin="round">
          <path d="M5 12c0-4 5-6 11-6s11 2 11 6l-4 1-1-3c-3-1-9-1-12 0l-1 3z" fill="#fff"/>
          <rect x="8" y="16" width="16" height="10" rx="2"/>
          <circle cx="16" cy="21" r="2.2" fill="#fff"/>
        </svg>
        <p>(07) 3321 0478<br>0412 555 019</p>
      </div>
      <div class="contact-panel__cell contact-panel__cell--web">
        <svg class="contact-panel__icon" viewBox="0 0 32 32" fill="none" stroke="#fff" stroke-width="1.8">
          <circle cx="16" cy="16" r="12"/>
          <ellipse cx="16" cy="16" rx="5.5" ry="12"/>
          <path d="M4 16h24M6 10h20M6 22h20"/>
        </svg>
        <p>hello@quillpresswash.com.au<br>www.quillpresswash.com.au</p>
      </div>
      <div class="contact-panel__cell contact-panel__cell--address">
        <svg class="contact-panel__icon" viewBox="0 0 32 32">
          <path d="M16 3a9 9 0 0 0-9 9c0 7 9 17 9 17s9-10 9-17a9 9 0 0 0-9-9z" fill="#fff"/>
          <circle cx="16" cy="12" r="3.4" fill="#323f91"/>
        </svg>
        <p>14 Wharf Street,<br>Brisbane QLD</p>
      </div>
    </div>
  </section>

  <section class="card card--brand">
    <div class="accent-band"></div>
    <div class="brand">
      <span class="brand__dot"></span>
      <span class="brand__name">Quill Press Wash</span>
    </div>
  </section>
</body>
</html>
```